Wordpress Website for electrician

I'm looking for an easy to maintain website for my electrical contracting business. Need a professional and appealing site.
Im wanting a website where clients can come on and look at services we offer, case studies and advertise our services.
Colours I'm wanting to incorporate are green, white, black and grey
I'm wanting a big slide show on main page where I can place advertising etc.
Menu is to include home, services, our work, specials, energy efficiency and contact
My existing site is www.trelwirefix.com.au
Updates
looking for something with a similar layout to this website
Target Market(s)
Businesses
Industry/Entity Type
Electrician
Look and feel

```html
<!DOCTYPE html>
<html lang="en">
<head>
<meta charset="utf-8">
<title>trelwirefix – electrical contractor</title>
<link href="https://fonts.googleapis.com/css2?family=PT+Sans:wght@400;700&family=Open+Sans:wght@300;400;700;800&display=swap" rel="stylesheet">
<style>
  :root {
    --page-bg: #ececec;
    --white: #ffffff;
    --green: #39b54a;
    --green-text: #3aa64a;
    --ink: #1a1a1a;
    --nav-bg: #231f20;
    --nav-line: #3d393a;
    --grey-text: #555555;
    --light-grey: #e6e6e6;
    --rule: #cfcfcf;
    --footer-bg: #050505;
  }
  * { margin: 0; padding: 0; box-sizing: border-box; }
  html, body { width: 1200px; height: 1000px; overflow: hidden; }
  body { background: var(--page-bg); font-family: "PT Sans", Arial, sans-serif; color: var(--ink); position: relative; }

  .top-phone { position: absolute; left: 775px; top: 10px; display: flex; align-items: center; gap: 10px; }
  .top-phone__number { font-family: "Open Sans", Arial, sans-serif; font-weight: 700; font-size: 28px; letter-spacing: 1px; color: var(--green-text); }

  .site { position: absolute; left: 197px; top: 55px; width: 806px; height: 945px; background: var(--white); box-shadow: 0 0 12px rgba(0,0,0,.35); }

  .brand { position: absolute; left: 16px; top: 20px; display: flex; align-items: center; gap: 12px; }
  .brand__dot { width: 30px; height: 30px; border-radius: 50%; background: var(--green); }
  .brand__name { font-size: 42px; font-weight: 400; color: var(--ink); line-height: 1; }
  .brand__tag { position: absolute; left: 145px; top: 66px; font-family: Arial, sans-serif; font-size: 12px; color: #777; letter-spacing: .5px; }

  .search { position: absolute; left: 579px; top: 37px; width: 217px; height: 34px; border: 2px solid #b5b5b5; border-radius: 6px; background: linear-gradient(#e2e2e2, #f4f4f4); }
  .search svg { position: absolute; right: 8px; top: 6px; }

  .main-nav { position: absolute; left: 8px; top: 116px; width: 789px; height: 39px; background: var(--nav-bg); border-radius: 4px; display: flex; }
  .main-nav a { color: var(--white); text-decoration: none; font-size: 13px; line-height: 39px; padding: 0 22px; border-right: 1px solid var(--nav-line); }
  .main-nav a:last-child { border-right: none; }

  .hero { position: absolute; left: 8px; top: 161px; width: 789px; height: 278px; background: linear-gradient(115deg, #2a1a3a 0%, #6a3a8a 25%, #3b3a36 50%, #6b5d3f 70%, #2e2a25 100%); }
  .hero__caption { position: absolute; right: 0; bottom: 0; width: 212px; height: 119px; background: rgba(40,40,40,.75); color: var(--white); font-family: "Open Sans", Arial, sans-serif; font-weight: 300; font-size: 38px; line-height: 48px; padding: 12px 0 0 36px; }

  .feature { position: absolute; left: 11px; top: 461px; width: 783px; height: 234px; background: linear-gradient(#e4e4e4, #ffffff); border-radius: 4px; }
  .intro { position: absolute; left: 21px; top: 16px; width: 240px; }
  .intro__title { font-family: "Open Sans", Arial, sans-serif; font-weight: 400; font-size: 26px; letter-spacing: -.5px; }
  .intro__body { margin-top: 20px; font-size: 11.5px; line-height: 18px; color: var(--ink); }

  .news { position: absolute; left: 296px; top: 30px; width: 190px; }
  .news__title { font-family: "Open Sans", Arial, sans-serif; font-size: 16px; padding-left: 4px; margin-bottom: 12px; }
  .news__item { font-family: Arial, sans-serif; font-size: 8.5px; line-height: 12px; color: #333; padding: 3px 10px 3px 10px; border-top: 1px solid var(--rule); }
  .news__item:last-child { border-bottom: 1px solid var(--rule); }
  .news__item--wide { width: 190px; }
  .news__list > .news__item:not(.news__item--wide) { width: 166px; }

  .promo { position: absolute; left: 499px; top: 10px; width: 272px; height: 217px; background: var(--white); text-align: center; }
  .promo__bulb { position: absolute; left: 113px; top: 12px; width: 38px; height: 64px; border-radius: 19px 19px 8px 8px; background: linear-gradient(#6aa84f, #555); }
  .promo__line1 { position: absolute; left: 0; right: 0; top: 78px; font-family: "Open Sans", Arial, sans-serif; font-weight: 800; font-size: 43px; color: var(--green); letter-spacing: -1px; }
  .promo__line2 { position: absolute; left: 0; right: 0; top: 120px; font-family: "Open Sans", Arial, sans-serif; font-weight: 800; font-size: 32px; color: var(--ink); letter-spacing: -.5px; }
  .promo__grass { position: absolute; left: 0; bottom: 0; width: 272px; height: 28px; background: linear-gradient(#7bbf4a, #2f6e1f); }

  .services { position: absolute; left: 0; top: 735px; width: 806px; height: 170px; }
  .service { position: absolute; top: 0; }
  .service__title { font-family: Arial, sans-serif; font-weight: 700; font-size: 19px; text-align: center; }
  .service__row { display: flex; gap: 6px; margin-top: 10px; }
  .service__icon { flex: 0 0 40px; height: 40px; }
  .service__text { font-family: Arial, sans-serif; font-size: 8.5px; line-height: 23px; color: #444; }
  .service__btn { position: absolute; top: 116px; width: 202px; height: 47px; background: var(--green); border-radius: 3px; color: var(--ink); font-family: "PT Sans", Arial, sans-serif; font-weight: 700; font-size: 15px; line-height: 47px; text-align: center; }
  .service-divider { position: absolute; top: 22px; width: 1px; height: 126px; background: #aaa; }

  .site-footer { position: absolute; left: 0; bottom: 0; width: 806px; height: 33px; background: var(--footer-bg); color: var(--white); font-family: "Open Sans", Arial, sans-serif; font-size: 11px; line-height: 33px; text-align: center; }
  .site-footer a { color: var(--green); text-decoration: none; }
</style>
</head>
<body>
  <div class="top-phone">
    <svg width="40" height="30" viewBox="0 0 40 30" aria-hidden="true">
      <path d="M2 10 Q20 -2 38 10 L35 15 L28 13 L28 9 Q20 6 12 9 L12 13 L5 15 Z" fill="#333"/>
      <rect x="8" y="14" width="24" height="15" rx="2" fill="#333"/>
      <circle cx="20" cy="21" r="5" fill="#ececec"/>
      <circle cx="20" cy="21" r="2" fill="#333"/>
    </svg>
    <span class="top-phone__number">0400 555 018</span>
  </div>

  <div class="site">
    <header>
      <div class="brand">
        <span class="brand__dot"></span>
        <span class="brand__name">trelwirefix</span>
      </div>
      <div class="brand__tag">electrical contractor</div>
      <div class="search">
        <svg width="22" height="22" viewBox="0 0 22 22" aria-hidden="true">
          <circle cx="9" cy="9" r="6.5" fill="none" stroke="#111" stroke-width="2.5"/>
          <line x1="14" y1="14" x2="20" y2="20" stroke="#111" stroke-width="3" stroke-linecap="round"/>
        </svg>
      </div>
      <nav class="main-nav">
        <a href="#">Home</a><a href="#">About</a><a href="#">Services</a><a href="#">Our Work</a><a href="#">Specials</a><a href="#">Energy Efficiency</a><a href="#">Contact</a>
      </nav>
    </header>

    <section class="hero" role="img" aria-label="Night photo of a lit terminal canopy with purple and white LED lighting">
      <div class="hero__caption">Energy<br>Efficient</div>
    </section>

    <section class="feature">
      <div class="intro">
        <h1 class="intro__title">LED IS THE FUTURE</h1>
        <p class="intro__body">LED lighting has involved rapidly in the last 5 years. In the coming years we will see all lighting being substitued with LED lights. It is by far the most efficient form of lighting on todays market. Let us retrofit your business or home with LED and the savings will literally pay the lights off.</p>
      </div>
      <div class="news">
        <h2 class="news__title">News</h2>
        <div class="news__list">
          <div class="news__item">Etiam ultricies nisi vel augue.<br>Etiam ultricies nisi vel augue.</div>
          <div class="news__item">Etiam ultricies nisi vel augue.<br>Etiam ultricies nisi vel augue.</div>
          <div class="news__item news__item--wide">Phasellus viverra nulla ut metus varius laoreet.<br>Quisque rutrum. Aenean imperdiet.<br>Etiam ultricies nisi vel augue.</div>
        </div>
      </div>
      <div class="promo">
        <div class="promo__bulb" role="img" aria-label="Light bulb with a small tree growing inside"></div>
        <div class="promo__line1">BE GREEN</div>
        <div class="promo__line2">SAVE MONEY</div>
        <div class="promo__grass" role="img" aria-label="Strip of green grass"></div>
      </div>
    </section>

    <section class="services">
      <div class="service" style="left:38px;width:210px;">
        <h3 class="service__title">Electrical Contracting</h3>
        <div class="service__row">
          <svg class="service__icon" viewBox="0 0 40 40" aria-hidden="true">
            <circle cx="20" cy="20" r="19" fill="#3b8f2f"/>
            <circle cx="20" cy="20" r="15" fill="#57b947"/>
            <path d="M14 14 A9 9 0 1 0 26 14" fill="none" stroke="#111" stroke-width="3" stroke-linecap="round"/>
            <line x1="20" y1="10" x2="20" y2="20" stroke="#111" stroke-width="3" stroke-linecap="round"/>
          </svg>
          <p class="service__text">We offer all types of electrical work from Installation to maintenance</p>
        </div>
        <div class="service__btn" style="left:0;">VIEW SERVICE</div>
      </div>
      <div class="service-divider" style="left:273px;"></div>
      <div class="service" style="left:296px;width:210px;">
        <h3 class="service__title">Energy Efficiency</h3>
        <div class="service__row">
          <svg class="service__icon" viewBox="0 0 40 40" aria-hidden="true">
            <circle cx="20" cy="20" r="19" fill="#3b8f2f"/>
            <circle cx="20" cy="20" r="15" fill="#57b947"/>
            <path d="M15 10 Q20 6 25 10 L25 24 L15 24 Z" fill="#fff"/>
            <rect x="16" y="25" width="8" height="5" fill="#ddd"/>
          </svg>
          <p class="service__text">With one of our audits to your business or home we can lower your energy bills and minimise your carbon footprint</p>
        </div>
        <div class="service__btn" style="left:8px;">VIEW SERVICE</div>
      </div>
      <div class="service-divider" style="left:531px;"></div>
      <div class="service" style="left:551px;width:215px;">
        <h3 class="service__title">Underground Locating</h3>
        <div class="service__row">
          <svg class="service__icon" viewBox="0 0 40 40" aria-hidden="true">
            <rect x="1" y="1" width="38" height="38" fill="#111"/>
            <circle cx="20" cy="20" r="15" fill="#fff" stroke="#d21f26" stroke-width="4"/>
            <rect x="17" y="12" width="6" height="14" fill="#111"/>
            <line x1="9" y1="9" x2="31" y2="31" stroke="#d21f26" stroke-width="4"/>
          </svg>
          <p class="service__text">We have the tools and knowledge in locating underground utilities.</p>
        </div>
        <div class="service__btn" style="left:5px;">VIEW SERVICE</div>
      </div>
    </section>

    <footer class="site-footer">Copyright © 2013 trelwirefix.com.au. <a href="#">Privacy Policy</a></footer>
  </div>
</body>
</html>
```